Business Card for Business consulting practice

Need a design for a consultant business card. Simple and elegant.
I need the following information on the card:
Logo: (see uploaded file)
Company name: Calmora Advisory Group
Name: Dana Weltrup
Title: Managing Director - Aerospace and Defence
Phone #: 514-268-3917
e-mail: dana.weltrup@calmora-example.com
Website: www.calmora-example.com
Tagline: Proposals Management and Capture support for complex procurements

```html
<!DOCTYPE html>
<html lang="en">
<head>
<meta charset="utf-8">
<title>Calmora Advisory Group – Business Card</title>
<link rel="stylesheet" href="https://fonts.googleapis.com/css2?family=Poppins:wght@400;500;700&display=swap">
<style>
  :root {
    --page-bg: #f2f2f2;
    --card-top: #1f1f1f;
    --card-bottom: #050505;
    --accent: #0a95bf;
    --text-light: #ffffff;
    --text-soft: #d9eef5;
  }
  * { box-sizing: border-box; margin: 0; padding: 0; }
  html, body {
    width: 1200px; height: 1200px; overflow: hidden;
    background: var(--page-bg);
    font-family: "Poppins", sans-serif;
  }
  .canvas { position: relative; width: 1200px; height: 1200px; }
  .card {
    position: absolute; left: 235px; width: 729px; height: 416px;
    background: linear-gradient(160deg, var(--card-top) 0%, var(--card-bottom) 100%);
    overflow: hidden;
    color: var(--text-light);
  }
  .card--front { top: 132px; }
  .card--back { top: 652px; }

  .pattern-area {
    position: absolute; inset: 0;
    background: linear-gradient(135deg, rgba(10,149,191,0) 45%, rgba(10,149,191,0.55) 72%, var(--accent) 100%);
    clip-path: polygon(100% 28%, 100% 100%, 33% 100%, 50% 66%, 78% 30%);
  }

  .tagline {
    position: absolute; left: 35px; top: 20px;
    font-size: 17.4px; font-weight: 400; letter-spacing: 0.1px; white-space: nowrap;
  }
  .company-name {
    position: absolute; left: 35px; top: 118px;
    font-size: 30px; font-weight: 500; letter-spacing: 0.5px; white-space: nowrap;
  }

  .person { position: absolute; left: 84px; top: 64px; }
  .person-name { font-size: 31px; font-weight: 700; line-height: 1.1; letter-spacing: 0.2px; }
  .person-title { margin-top: 4px; font-size: 16.5px; font-weight: 400; line-height: 21px; color: var(--text-soft); }
  .title-rule {
    margin-top: 6px; width: 231px; height: 3px;
    background: linear-gradient(90deg, var(--accent) 0 40px, var(--text-light) 40px 100%);
  }

  .contact-bar {
    position: absolute; left: 81px; top: 246px; width: 32px; height: 102px;
    background: var(--accent);
  }
  .contact-bar svg { position: absolute; left: 8px; width: 16px; height: 16px; fill: #111; }
  .contact-list { position: absolute; left: 120px; top: 250px; list-style: none; font-size: 16px; line-height: 1; }
  .contact-list li { position: absolute; white-space: nowrap; }
</style>
</head>
<body>
<main class="canvas">
  <section class="card card--front">
    <div class="pattern-area" role="img" aria-label="Decorative blue triangle pattern"></div>
    <p class="tagline">Proposals Management and Capture support for complex procurements</p>
    <h1 class="company-name">Calmora Advisory Group</h1>
  </section>

  <section class="card card--back">
    <div class="pattern-area" role="img" aria-label="Decorative blue triangle pattern"></div>
    <div class="person">
      <h2 class="person-name">DANA WELTRUP</h2>
      <p class="person-title">Managing Director -<br>Aerospace and Defence</p>
      <div class="title-rule"></div>
    </div>

    <div class="contact-bar">
      <svg style="top:9px" viewBox="0 0 24 24" aria-hidden="true"><path d="M6.6 10.8a15.1 15.1 0 0 0 6.6 6.6l2.2-2.2a1 1 0 0 1 1-.25 11.4 11.4 0 0 0 3.6.57 1 1 0 0 1 1 1V20a1 1 0 0 1-1 1A17 17 0 0 1 3 4a1 1 0 0 1 1-1h3.5a1 1 0 0 1 1 1c0 1.25.2 2.45.57 3.57a1 1 0 0 1-.25 1z"/></svg>
      <svg style="top:43px" viewBox="0 0 24 24" aria-hidden="true"><path d="M2 5h20v14H2z M3.5 6.5v11h17v-11l-8.5 6z M4.5 6.5 12 11.8l7.5-5.3z" fill-rule="evenodd"/></svg>
      <svg style="top:77px" viewBox="0 0 24 24" aria-hidden="true"><path d="M6 2v18l4.5-4.3 3 6.3 2.6-1.2-3-6.2H19z"/></svg>
    </div>
    <ul class="contact-list">
      <li style="top:0">514-268-3917</li>
      <li style="top:32px">dana.weltrup@calmora-example.com</li>
      <li style="top:68px">www.calmora-example.com</li>
    </ul>
  </section>
</main>
</body>
</html>
```